Design some Double Sided Business Cards

***FINAL FILES NEED TO BE SUBMITTED AS LAYERED PSD FILES***

Create a business card for a Home Repair company (logo attached). One side should include logo and contact info (ONLY Name, phone number & email) and the other side should list the services offered (put into 3 columns - 6 services in each column)

For your mockup use this contact info:
Rod Pemberton
555-472-9360
RodPemberton@[url removed, login to view]

Here are the list of services to add on the back (you can reorder these if need be for spacing reasons):
Flooring
Electric Repairs
Running Wires
Installing Interior/Exterior Lights
Appliance Repairs
Ac Repairs
Painting & Drywall
Counter Tops
Woodwork
Roofing
Plumbing
Tubs & Tile
Demolition
Renovations
Decks
Fences
Window Install & Window Repairs
Custom Interior/Exterior Installs & Designs

```html
<!DOCTYPE html>
<html lang="en">
<head>
<meta charset="utf-8">
<title>Crestline Repair – Business Cards</title>
<link rel="stylesheet" href="https://fonts.googleapis.com/css2?family=Cinzel:wght@500;600&family=Lato:wght@400;700&display=swap">
<style>
  :root {
    --page-bg: #e4e6e7;
    --card-white: #ffffff;
    --ink-dark: #3a3435;
    --ink-teal: #173c43;
    --maroon: #5e1e1e;
    --panel-grey: #38393b;
    --panel-teal: #0e3a42;
    --mint: #4fc3b0;
    --text-light: #f2f5f5;
  }
  * { box-sizing: border-box; margin: 0; padding: 0; }
  html, body { width: 1200px; height: 900px; overflow: hidden; }
  body { background: var(--page-bg); position: relative; font-family: "Lato", sans-serif; }

  .card {
    position: absolute;
    top: 296px;
    width: 540px;
    height: 309px;
    background: var(--card-white);
    box-shadow: 0 6px 18px rgba(0,0,0,.18);
    overflow: hidden;
  }
  .card--front { left: 40px; }
  .card--back { left: 620px; }

  /* Front */
  .holder { position: absolute; left: 40px; top: 34px; }
  .holder__name {
    font-family: "Cinzel", serif; font-weight: 600; font-size: 19px;
    letter-spacing: 1.5px; color: var(--ink-teal);
  }
  .holder__role {
    font-family: "Lato", sans-serif; font-size: 12px; color: var(--ink-dark);
    margin-top: 4px; padding-left: 58px;
  }
  .contact { position: absolute; left: 40px; top: 104px; display: flex; gap: 12px; align-items: flex-start; }
  .contact__icons {
    width: 34px; height: 34px; border-radius: 5px; background: var(--ink-teal);
    display: flex; align-items: center; justify-content: center;
  }
  .contact__lines { font-size: 11.5px; color: var(--ink-dark); line-height: 17px; padding-top: 2px; }

  .brand {
    position: absolute; right: 34px; top: 150px;
    display: flex; align-items: center; gap: 12px;
  }
  .brand__mark { width: 22px; height: 22px; background: var(--maroon); }
  .brand__name {
    font-family: "Cinzel", serif; font-weight: 500; font-size: 30px; line-height: 32px;
    letter-spacing: 2px; color: var(--ink-dark); text-transform: uppercase; text-align: right;
  }

  .band { position: absolute; left: 0; right: 0; background: var(--ink-teal); }
  .band--thick { top: 262px; height: 13px; }
  .band--thin { top: 280px; height: 5px; }

  /* Back */
  .panel {
    position: absolute; inset: 16px; border-radius: 12px; background: var(--panel-grey);
  }
  .panel__inner {
    position: absolute; inset: 12px; background: var(--panel-teal);
    border: 2px solid var(--mint);
  }
  .tools {
    position: absolute; right: 96px; top: 14px; width: 46px; height: 46px; border-radius: 4px;
    background: linear-gradient(135deg, #e8ecec, #6ec9b9);
  }
  .services { position: absolute; list-style: none; color: var(--text-light); font-size: 10.5px; line-height: 15px; }
  .services li { position: relative; padding-left: 16px; }
  .services li::before {
    content: ""; position: absolute; left: 0; top: 3px; width: 10px; height: 10px;
    border-radius: 50%; background: var(--text-light);
  }
  .services li::after {
    content: ""; position: absolute; left: 4px; top: 5.5px;
    border-left: 4px solid var(--panel-teal); border-top: 2.5px solid transparent; border-bottom: 2.5px solid transparent;
  }
  .services--one { left: 18px; top: 18px; }
  .services--two { left: 118px; top: 18px; }
  .services--three { left: 318px; top: 108px; }
</style>
</head>
<body>

  <section class="card card--front" aria-label="Business card front">
    <div class="holder">
      <p class="holder__name">Rod Pemberton</p>
      <p class="holder__role">Service Manager</p>
    </div>

    <div class="contact">
      <div class="contact__icons" aria-hidden="true">
        <svg width="24" height="24" viewBox="0 0 24 24">
          <rect x="3" y="2" width="8" height="13" rx="1.5" fill="none" stroke="#fff" stroke-width="1.5"/>
          <rect x="11" y="12" width="11" height="8" rx="1" fill="#fff"/>
          <path d="M11 12 L16.5 16.5 L22 12" fill="none" stroke="#173c43" stroke-width="1.2"/>
        </svg>
      </div>
      <div class="contact__lines">
        <p class="contact__phone">555-472-9360</p>
        <p class="contact__email">RodPemberton@homemend.com</p>
      </div>
    </div>

    <div class="brand">
      <span class="brand__mark" aria-hidden="true"></span>
      <p class="brand__name">Crestline<br>Repair</p>
    </div>

    <div class="band band--thick"></div>
    <div class="band band--thin"></div>
  </section>

  <section class="card card--back" aria-label="Business card back">
    <div class="panel">
      <div class="panel__inner">
        <div class="tools" role="img" aria-label="Crossed wrench and screwdriver illustration"></div>

        <ul class="services services--one">
          <li>Flooring</li>
          <li>Roofing</li>
          <li>Plumbing</li>
          <li>Decks</li>
          <li>Fences</li>
        </ul>

        <ul class="services services--two">
          <li>Electric Repairs</li>
          <li>AC Repairs</li>
          <li>Running Wires</li>
          <li>Appliance repairs</li>
          <li>Painting and Drywall</li>
          <li>Installing Interior/Exterior Lights</li>
          <li>Window Install and Window Repairs</li>
          <li>Custom Interior/Exterior Installs</li>
        </ul>

        <ul class="services services--three">
          <li>Woodwork</li>
          <li>Tubs and Tiles</li>
          <li>Counter Tops</li>
          <li>Demolition</li>
          <li>Renovations</li>
        </ul>
      </div>
    </div>
  </section>

</body>
</html>
```